Restaurant, Nightclub

It's a Restaurant come nightclub. Our sign Lumen is white letters with blue edging on a black back ground.

Industry/Entity Type

Restaurant

Contact Information for Business Card

Lumen Stevenage Ltd
42 Mill Lane
Stevenage Herts SG2 7PQ

```html
<!DOCTYPE html>
<html lang="en">
<head>
<meta charset="utf-8">
<title>Lumen Stevenage Ltd – Business Card</title>
<link rel="stylesheet" href="https://fonts.googleapis.com/css2?family=Arimo:wght@400;700&display=swap">
<style>
  :root {
    --card-bg: #161718;
    --card-bg-light: #1f2021;
    --disc-fill: #0b0c0d;
    --disc-edge: #1c1d1e;
    --text-white: #ffffff;
    --text-grey: #8c9194;
  }
  html, body {
    margin: 0;
    padding: 0;
    width: 1200px;
    height: 791px;
    overflow: hidden;
    background: var(--card-bg);
  }
  .card {
    position: relative;
    width: 1200px;
    height: 791px;
    overflow: hidden;
    font-family: "Arimo", Arial, sans-serif;
    background: radial-gradient(ellipse at 50% 45%, var(--card-bg-light) 0%, var(--card-bg) 70%);
  }
  .emblem-disc {
    position: absolute;
    left: 355px;
    top: 102px;
    width: 490px;
    height: 490px;
    border-radius: 50%;
    background: var(--disc-fill);
    box-shadow: 0 0 0 1px var(--disc-edge);
  }
  .brand-name {
    position: absolute;
    left: 0;
    width: 1200px;
    top: 268px;
    margin: 0;
    text-align: center;
    font-weight: 700;
    font-size: 150px;
    line-height: 150px;
    letter-spacing: -2px;
    color: var(--text-white);
  }
  .company-name {
    position: absolute;
    left: 0;
    width: 1200px;
    top: 615px;
    margin: 0;
    text-align: center;
    font-weight: 400;
    font-size: 31px;
    line-height: 36px;
    color: var(--text-white);
  }
  .company-address {
    position: absolute;
    left: 0;
    width: 1200px;
    top: 657px;
    margin: 0;
    text-align: center;
    font-weight: 400;
    font-size: 17px;
    line-height: 22px;
    letter-spacing: 2.2px;
    color: var(--text-grey);
  }
  .company-phone {
    position: absolute;
    left: 0;
    width: 1200px;
    top: 710px;
    margin: 0;
    text-align: center;
    font-weight: 400;
    font-size: 23px;
    line-height: 28px;
    color: var(--text-white);
  }
</style>
</head>
<body>
  <main class="card">
    <div class="emblem-disc"></div>
    <h1 class="brand-name">Lumen</h1>
    <p class="company-name">Lumen Stevenage Ltd</p>
    <p class="company-address">42 Mill Lane Stevenage Herts SG2 7PQ</p>
    <p class="company-phone">Ph: 000 5678 910</p>
  </main>
</body>
</html>
```